Menu Design Project for new restauranct concept

Design menu for new restaurant concept called Juniper's Burgers & Dogs. Logo is attached.

Industry/Entity Type

Restaurant

Requirements
Must have
• Menu items and pricing:

Burgers
Snack Burger $3.49
Snack Cheeseburger $3.99
Juniper's signature Burger $4.99
Juniper's signature Cheeseburger $5.49
Burger toppings: bacon, lettuce, tomato, onion, pickle, grilled onions, grilled mushrooms, grilled green peppers, jalapeƱo peppers.

Dogs
Hot Dog $2.99
Bacon Cheese Hot Dog $3.99
Slaw Dog $3.99
Kraut Dog $3.49
Chili Dog $3.99 with or with out cheese
Hot dogs are 100% beef

Other
Grilled Chicken Sandwich $5.99
Grilled Chicken Sandwich with cheese $6.49
(Same toppings as burgers)

French Fries $1.99

Loaded Potatos
The Plain Tater: $4.99 choose from: butter, sour cream, cheese, chives
The Garden Tater: $5.99 choose from: the Basic plus, broccoli & cheese, grilled mushrooms, onions, & peppers
The Carver Tater: $6.99 choose from the Basic/Veggie plus: grilled chicken, chili, Philly cheesesteak, pulled pork.

Drinks
32oz. Drink $1.88
20oz. Drink $1.69

attached logo.
Nice to have
• love to incorporate the woodgrain backgound. It makes the logo look most like a cattle brand, which we like.

```html
<!DOCTYPE html>
<html lang="en">
<head>
<meta charset="utf-8">
<title>Juniper's Burgers &amp; Dogs Menu</title>
<link rel="stylesheet" href="https://fonts.googleapis.com/css2?family=Montserrat:wght@800;900&display=swap">
<style>
:root{
  --wood-light:#9a9087;
  --wood-mid:#8a8078;
  --wood-dark:#776d66;
  --ink:#0d0d0d;
  --rule:#3a332e;
  --panel:#ffffff;
}
html,body{margin:0;padding:0;overflow:hidden;}
body{width:927px;height:1200px;font-family:'Montserrat',Arial,sans-serif;color:var(--ink);}
.menu{position:relative;width:927px;height:1200px;overflow:hidden;}
.woodgrain{position:absolute;inset:0;background:linear-gradient(180deg,var(--wood-light) 0%,var(--wood-mid) 55%,var(--wood-dark) 100%);}
.column{position:absolute;top:42px;height:1124px;border:2px solid var(--rule);box-sizing:border-box;text-align:center;font-weight:900;}
.column--burgers{left:42px;width:270px;}
.column--dogs{left:612px;width:297px;}
.column-title{font-size:54px;line-height:1;margin:30px 0 44px;letter-spacing:-0.5px;}
.item{font-size:30px;line-height:1.2;margin:0 0 28px;letter-spacing:-0.3px;}
.item--lead{font-size:31px;line-height:1.18;margin-bottom:30px;}
.toppings{font-size:23px;line-height:1.3;margin:44px 10px 0 12px;font-weight:800;}
.dogs-note{font-size:16px;font-weight:800;margin:-14px 0 30px;}
.dogs-claim{font-size:43px;line-height:1.15;margin:0;}
.brand-name{position:absolute;margin:0;text-align:center;font-weight:900;color:var(--ink);}
.brand-name--top{left:316px;top:140px;width:290px;font-size:32px;line-height:1.25;}
.brand-name--foot{left:660px;top:985px;width:206px;font-size:22px;line-height:1.25;}
.panel-other{position:absolute;left:321px;top:382px;width:288px;height:818px;background:var(--panel);text-align:center;font-weight:800;padding-top:8px;box-sizing:border-box;}
.panel-title{font-size:30px;font-weight:900;margin:0 0 18px;}
.entry{font-size:22px;line-height:1.15;margin:0 0 20px;}
.entry small{display:block;font-size:16px;line-height:1.25;}
.spud{margin:0 10px 22px;}
.spud-name{font-size:22px;line-height:1.2;margin:0;}
.spud-desc{font-size:17px;line-height:1.3;margin:0;}
.drinks{font-size:22px;line-height:1.4;margin:12px 0 0;}
.drinks span{display:block;font-size:19px;}
</style>
</head>
<body>
<main class="menu">
  <div class="woodgrain" role="img" aria-label="Weathered grey woodgrain background"></div>

  <section class="column column--burgers">
    <h2 class="column-title">Burgers</h2>
    <p class="item">Snack Burger<br>$3.49</p>
    <p class="item">Snack<br>Cheeseburger<br>$3.99</p>
    <p class="item item--lead">Juniper's<br>Signature Burger<br>$4.99</p>
    <p class="item item--lead">Juniper's<br>Signature<br>Cheeseburger<br>$5.49</p>
    <p class="toppings">Burger toppings: bacon, lettuce, tomato, onion, pickle, grilled onions, grilled mushrooms, grilled green peppers, jalapeño peppers.</p>
  </section>

  <p class="brand-name brand-name--top">Juniper's<br>Burgers &amp; Dogs</p>

  <section class="panel-other">
    <h2 class="panel-title">Other</h2>
    <p class="entry">Grilled Chicken<small>Sandwich $5.99<br>Grilled Chicken Sandwich<br>with cheese $6.49<br>(Same toppings as burgers)</small></p>
    <p class="entry">French Fries $1.99</p>
    <p class="entry">Loaded Potatos</p>
    <div class="spud">
      <p class="spud-name">The Plain Tater:</p>
      <p class="spud-desc">$4.99 choose from: butter, sour cream, cheese, chives</p>
    </div>
    <div class="spud">
      <p class="spud-name">The Garden Tater:</p>
      <p class="spud-desc">$5.99 choose from: the Basic plus, broccoli &amp; cheese, grilled mushrooms, onions, &amp; peppers</p>
    </div>
    <div class="spud">
      <p class="spud-name">The Carver Tater:</p>
      <p class="spud-desc">$6.99 choose from the Basic/Veggie plus: grilled chicken, chili, Philly cheesesteak, pulled pork.</p>
    </div>
    <p class="drinks">Drinks<span>32oz. Drink $1.88</span><span>20oz. Drink $1.69</span></p>
  </section>

  <section class="column column--dogs">
    <h2 class="column-title">Dogs</h2>
    <p class="item">Hot Dog<br>$2.99</p>
    <p class="item">Bacon Cheese<br>Hot Dog $3.99</p>
    <p class="item">Slaw Dog $<br>3.99</p>
    <p class="item">Kraut Dog<br>$3.49</p>
    <p class="item">Chili Dog<br>$3.99</p>
    <p class="dogs-note">with or with out cheese</p>
    <p class="dogs-claim">Hot dogs<br>are 100%<br>beef</p>
  </section>

  <p class="brand-name brand-name--foot">Juniper's<br>Burgers &amp; Dogs</p>
</main>
</body>
</html>
```